Flyer Design

I recently got a website designed by Pagecrest - www.tidynestliving.com.au

I own an organisational business. We help people to simplify their homes which in turn, creates a more balanced and healthy life. We offer de-clutter services for pantries, wardrobes, linen cupboards, home offices, and anywhere you need a bit of organisation. We can help you with de-cluttering and property styling that will help to sell your home. In addition, we provide help with moving, packing and unpacking, or even downsizing. With our keen eye for detail and passion for interior design, we will not only provide a practical solution, but a wonderful design element to your home. Tidy Nest Living is a proud member of the Southern Guild of Certified Space Planners Inc.

Can I please use the logo off my website. I have also put it below.

Industry/Entity Type

Business

```html
<!DOCTYPE html>
<html lang="en">
<head>
<meta charset="utf-8">
<title>Tidy Nest Living – Flyer</title>
<link rel="stylesheet" href="https://fonts.googleapis.com/css2?family=Source+Sans+3:ital,wght@0,400;0,600;1,400&display=swap">
<style>
  :root {
    --teal: #6cc5d1;
    --teal-light: #86d3dd;
    --ink: #1e1e1e;
    --band: rgba(40, 40, 40, 0.88);
    --body-grey: #7a7a7a;
    --heading: #2b2b2b;
    --frame: #cfcfcf;
    --paper: #ffffff;
  }
  * { margin: 0; padding: 0; box-sizing: border-box; }
  html, body { width: 907px; height: 1200px; overflow: hidden; background: var(--paper); }
  body { font-family: "Source Sans 3", "Myriad Pro", sans-serif; }

  .flyer { position: relative; width: 907px; height: 1200px; background: var(--paper); }

  .hero {
    position: absolute; left: 0; top: 0; width: 907px; height: 540px;
    background: linear-gradient(100deg, #e9e9e6 0%, #d7dcdf 30%, #b9c6cc 55%, #d9e1e4 75%, #8d969a 100%);
  }
  .hero-band {
    position: absolute; left: 0; top: 426px; width: 907px; height: 114px;
    background: var(--band);
  }
  .brand {
    position: absolute; left: 44px; top: 452px; display: flex; align-items: center; gap: 18px;
  }
  .brand-mark { width: 56px; height: 56px; background: var(--teal); }
  .brand-name {
    font-weight: 600; font-size: 42px; color: #ffffff; letter-spacing: 0.5px; line-height: 1;
  }

  .gallery { position: absolute; top: 576px; left: 58px; display: flex; gap: 28px; }
  .gallery-item { width: 247px; height: 180px; border: 2px solid var(--frame); }
  .gallery-item.office { background: linear-gradient(160deg, #d9d4cc 0%, #8a5a3a 55%, #2c2c2c 100%); }
  .gallery-item.linen { background: linear-gradient(90deg, #f3f1ec 0%, #e7e2d8 40%, #c9a877 100%); }
  .gallery-item.lounge { background: linear-gradient(160deg, #e8e6e2 0%, #f4f2ef 50%, #d65a6d 80%, #3a3a3a 100%); }

  .content { position: absolute; left: 32px; top: 786px; width: 843px; }
  .content h1 {
    font-weight: 400; font-size: 26px; color: var(--heading); margin-bottom: 14px;
  }
  .content p {
    font-size: 17.5px; line-height: 1.3; color: var(--body-grey); text-align: justify; margin-bottom: 11px;
  }

  .phone-block {
    position: absolute; left: 0; top: 1094px; width: 370px; height: 106px;
  }
  .phone-block svg.shape { position: absolute; left: 0; top: 0; }
  .phone-line {
    position: absolute; left: 30px; top: 44px; display: flex; align-items: center; gap: 16px;
    font-size: 31px; color: var(--ink); letter-spacing: 1px;
  }

  .membership {
    position: absolute; left: 412px; top: 1099px; width: 380px;
    font-style: italic; font-size: 13.5px; line-height: 1.25; color: #555;
  }
  .badge {
    position: absolute; left: 806px; top: 1052px; width: 66px; height: 86px;
    border: 2px solid #555; background: #fff;
  }

  .web-bar {
    position: absolute; left: 363px; top: 1147px; width: 544px; height: 53px; background: #050505;
    display: flex; align-items: center; justify-content: center;
  }
  .web-bar a {
    color: var(--teal-light); text-decoration: none; font-size: 23px; letter-spacing: 2px;
  }
</style>
</head>
<body>
  <main class="flyer">
    <div class="hero" role="img" aria-label="Photo of a bright attic living room with white brick wall, framed prints, grey chaise lounge and built-in drawers"></div>
    <div class="hero-band">
    </div>
    <div class="brand">
      <span class="brand-mark"></span>
      <span class="brand-name">Tidy Nest Living</span>
    </div>

    <section class="gallery">
      <div class="gallery-item office" role="img" aria-label="Photo of an organised home office desk and shelves"></div>
      <div class="gallery-item linen" role="img" aria-label="Photo of a neatly stacked linen cupboard with baskets"></div>
      <div class="gallery-item lounge" role="img" aria-label="Photo of a styled reading corner with bookshelves and armchair"></div>
    </section>

    <section class="content">
      <h1>Uncluttering Life – One Home at a Time</h1>
      <p>At Tidy Nest Living, we help you to organise your life. We work with busy working families who do not typically have time to organise their homes.</p>
      <p>We offer de-clutter services for pantries, wardrobes, linen cupboards, home offices, and anywhere you need a bit of organisation.</p>
      <p>We can help you with de-cluttering and property styling that will help to sell your home. In addition, we provide help with moving, packing and unpacking, or even downsizing.</p>
      <p>With our keen eye for detail and passion for interior design, we will not only provide a practical solution, but a wonderful design element to your home.</p>
    </section>

    <div class="phone-block">
      <svg class="shape" width="370" height="106" viewBox="0 0 370 106" aria-hidden="true">
        <polygon points="0,0 350,0 370,53 370,106 0,106" fill="var(--teal)"/>
      </svg>
      <div class="phone-line">
        <svg width="42" height="42" viewBox="0 0 42 42" aria-hidden="true">
          <circle cx="21" cy="21" r="19" fill="none" stroke="#1e1e1e" stroke-width="2.5"/>
          <path d="M14 11c1.5-1 3-.5 3.6.8l1.6 3.4c.5 1 .2 2-.6 2.6l-1.4 1c1 2.6 3 4.8 5.6 6l1.1-1.3c.7-.8 1.7-1 2.6-.5l3.3 1.8c1.2.7 1.5 2.2.6 3.6-1.6 2.4-4 3-6.6 2-6.4-2.4-10.6-7-12.4-13-.7-2.5.2-5 2.6-6.4z" fill="#1e1e1e"/>
        </svg>
        <span>0412358690</span>
      </div>
    </div>

    <p class="membership">Tidy Nest Living is a proud member of the<br>Southern Guild of Certified Space Planners Inc.</p>
    <div class="badge" role="img" aria-label="Membership badge"></div>

    <div class="web-bar"><a href="#">www.tidynestliving.com.au</a></div>
  </main>
</body>
</html>
```